Infographic Customizable and DISC Proof

Design of an infographic used to assist candidates to get an overview on the steps they need to take in order to get the candidate in the best possible position to a new step in their career.

Attached is an outline of the text that needs to be converted to an Infographic.

The infographics will be used predominantly as an attachment in the email from the recruiter to the candidate.

Based on the DISC profile of the candidate we require 2 different designs; 1 designed for yellow disc profiles, stylish, beautifull, with the use of our brand color scheme. And one more factual for example for a blue disc profile with far less or no use of colour and a more sleek clean design.

It is important to take into consideration with your design and format you deliver that we want to be able to change some of the content on the infographics after your delivery completely by ourselves for the following use cases:

1. processes differ per client, hence we must be able to add or remove a step and be able to change the title and body of the steps in order to create an infographic for a different client of ours.
2. We would like to be able to change contact details and the profile picture of the recruiter. Example of a profile picture we would want to use is similar to the profile picture of a crestloop profile but then without the background. I attached it as an example for your reference.

It's important to take into consideration that we would need to be able to make such changes by ourselves without the need to become a savvy user of programs such as paint or adobe. The person that would need to be able to make the change is a recruiter, a typical office worker. Please let us know how we would be enabled to do this when you completed the design.

```html
<!DOCTYPE html>
<html lang="nl">
<head>
<meta charset="utf-8">
<title>In 4 stappen optimaal voor het voetlicht</title>
<link href="https://fonts.googleapis.com/css2?family=Oswald:wght@500;700&family=Open+Sans:wght@400;600;700&display=swap" rel="stylesheet">
<style>
  :root{
    --blue:#1f5fa8;
    --blue-dark:#163f73;
    --orange:#f08a12;
    --orange-dark:#d9700a;
    --grey-bar:#eef0f3;
    --grey-box:#5b6b80;
    --text:#2a2f38;
    --white:#ffffff;
  }
  *{margin:0;padding:0;box-sizing:border-box}
  html,body{width:709px;height:1200px;overflow:hidden;background:var(--white)}
  body{font-family:"Open Sans",Arial,sans-serif;color:var(--text);position:relative}

  .header{position:absolute;left:0;top:0;width:709px;height:230px}
  .header svg{position:absolute;left:0;top:0}
  .header-title{position:absolute;top:30px;width:100%;text-align:center;font-family:"Oswald",Arial,sans-serif;font-weight:500;font-size:38px;color:var(--white);letter-spacing:1px}
  .header-banner{position:absolute;left:58px;top:92px;width:593px;height:70px;background:var(--orange);border-radius:8px;display:flex;align-items:center;justify-content:center;font-family:"Oswald",Arial,sans-serif;font-weight:700;font-size:46px;color:var(--white);letter-spacing:1px;box-shadow:0 4px 0 var(--orange-dark)}

  .step{position:absolute;left:28px;width:655px}
  .step-badge{position:absolute;left:0;top:0;width:120px;height:120px}
  .step-title{position:absolute;left:142px;top:14px;width:513px;height:44px;background:var(--grey-bar);border-radius:4px;display:flex;align-items:center;padding-left:18px;font-weight:700;font-size:20px}
  .step-icon{position:absolute;right:0;top:-4px;width:52px;height:52px;border-radius:6px;display:flex;align-items:center;justify-content:center}
  .step.blue .step-icon{background:var(--blue)}
  .step.orange .step-icon{background:var(--orange)}
  .step-list{position:absolute;left:150px;top:70px;list-style:none;font-size:13.5px;line-height:21px}
  .step-list li{position:relative;padding-left:20px}
  .step-list li::before{content:"";position:absolute;left:0;top:6px;width:9px;height:9px;background:var(--blue)}
  .step.orange .step-list li::before{background:var(--orange)}

  .extra{position:absolute;left:40px;top:902px;width:629px;height:82px;background:var(--grey-box);border-radius:6px}
  .extra-label{position:absolute;left:-8px;top:-14px;background:var(--blue);color:var(--white);font-weight:700;font-size:16px;padding:5px 16px;border-radius:4px}
  .extra-list{position:absolute;left:22px;top:26px;list-style:none;color:var(--white);font-size:13.5px;line-height:24px}
  .extra-list li{position:relative;padding-left:20px}
  .extra-list li::before{content:"";position:absolute;left:0;top:8px;width:9px;height:9px;background:var(--orange)}

  .tagline{position:absolute;top:998px;width:100%;text-align:center;font-family:"Oswald",Arial,sans-serif;font-weight:700;font-size:30px;color:var(--blue-dark);letter-spacing:1px}
  .tagline span{color:var(--orange)}

  .footer{position:absolute;left:0;top:1056px;width:709px;height:120px}
  .recruiter-photo{position:absolute;left:52px;top:0;width:104px;height:104px;border-radius:50%;background:linear-gradient(160deg,#d8dde4,#9aa6b4);border:4px solid var(--orange)}
  .recruiter-name{position:absolute;left:168px;top:8px;background:var(--orange);color:var(--white);padding:4px 14px;border-radius:4px;font-weight:700;font-size:17px;line-height:20px}
  .recruiter-name small{display:block;font-weight:400;font-size:12px;line-height:14px}
  .contact{position:absolute;left:172px;font-size:15px;font-weight:600;color:var(--blue-dark);display:flex;align-items:center;gap:8px}
  .contact.phone{top:62px}
  .contact.mail{top:86px}
  .brand{position:absolute;right:50px;top:34px;display:flex;align-items:center;gap:10px;font-weight:700;font-size:30px;color:var(--blue-dark);letter-spacing:1px}
  .brand-mark{width:30px;height:30px;background:var(--orange)}
</style>
</head>
<body>

<header class="header">
  <svg width="709" height="230" viewBox="0 0 709 230">
    <path d="M0 0H709V180Q354 240 0 180Z" fill="var(--blue)"/>
  </svg>
  <h1 class="header-title">IN 4 STAPPEN OPTIMAAL</h1>
  <div class="header-banner">VOOR HET VOETLICHT</div>
</header>

<section class="step blue" style="top:240px">
  <svg class="step-badge" viewBox="0 0 124 124">
    <path d="M62 6A56 56 0 1 0 118 62" fill="none" stroke="var(--blue)" stroke-width="6"/>
    <circle cx="62" cy="62" r="46" fill="var(--blue)"/>
    <text x="62" y="50" text-anchor="middle" font-family="Oswald, sans-serif" font-size="14" fill="#fff">STEP</text>
    <text x="62" y="84" text-anchor="middle" font-family="Oswald, sans-serif" font-weight="700" font-size="34" fill="#fff">01</text>
  </svg>
  <div class="step-title">CV voorbereiden
    <div class="step-icon"><svg width="26" height="30" viewBox="0 0 26 30"><rect x="2" y="2" width="22" height="26" rx="2" fill="#fff"/><rect x="6" y="8" width="14" height="2" fill="var(--blue)"/><rect x="6" y="14" width="14" height="2" fill="var(--blue)"/><rect x="6" y="20" width="9" height="2" fill="var(--blue)"/></svg></div>
  </div>
  <ul class="step-list">
    <li>Gebruik het bijgevoegde CV-template</li>
    <li>Maximaal 7 pagina's A4</li>
    <li>Schrijf in het Nederlands</li>
    <li>Volg de specifieke datumnotatie [dd-mm-jj]</li>
    <li>Vermeld uren per week bij elke functie in het werkverleden</li>
    <li>Voeg blokken toe waar nodig</li>
  </ul>
</section>

<section class="step orange" style="top:450px">
  <svg class="step-badge" viewBox="0 0 124 124">
    <path d="M62 6A56 56 0 1 0 118 62" fill="none" stroke="var(--orange)" stroke-width="6"/>
    <circle cx="62" cy="62" r="46" fill="var(--orange)"/>
    <text x="62" y="50" text-anchor="middle" font-family="Oswald, sans-serif" font-size="14" fill="#fff">STEP</text>
    <text x="62" y="84" text-anchor="middle" font-family="Oswald, sans-serif" font-weight="700" font-size="34" fill="#fff">02</text>
  </svg>
  <div class="step-title">Eisen en wensen beargumenteren
    <div class="step-icon"><svg width="28" height="30" viewBox="0 0 28 30"><rect x="2" y="2" width="20" height="26" rx="2" fill="#fff"/><path d="M6 10l2 2 4-4M6 19l2 2 4-4" stroke="var(--orange)" stroke-width="2" fill="none"/><rect x="14" y="10" width="5" height="2" fill="var(--orange)"/><rect x="14" y="19" width="5" height="2" fill="var(--orange)"/></svg></div>
  </div>
  <ul class="step-list">
    <li>Beargumenteer eisen beknopt en herleidbaar</li>
    <li>Beargumenteer wensen uitgebreid en kwalitatief</li>
    <li>Geef situatieschetsen en voorbeelden van ervaring</li>
    <li>Vermeld het aantal maanden ervaring per gevraagd element</li>
  </ul>
</section>

<section class="step blue" style="top:618px">
  <svg class="step-badge" viewBox="0 0 124 124">
    <path d="M62 6A56 56 0 1 0 118 62" fill="none" stroke="var(--blue)" stroke-width="6"/>
    <circle cx="62" cy="62" r="46" fill="var(--blue)"/>
    <text x="62" y="50" text-anchor="middle" font-family="Oswald, sans-serif" font-size="14" fill="#fff">STEP</text>
    <text x="62" y="84" text-anchor="middle" font-family="Oswald, sans-serif" font-weight="700" font-size="34" fill="#fff">03</text>
  </svg>
  <div class="step-title">Motivatie en introductie
    <div class="step-icon"><svg width="30" height="28" viewBox="0 0 30 28"><circle cx="10" cy="8" r="5" fill="#fff"/><path d="M1 26c0-7 4-10 9-10s9 3 9 10z" fill="#fff"/><rect x="20" y="4" width="9" height="7" rx="1" fill="#fff"/></svg></div>
  </div>
  <ul class="step-list">
    <li>Schrijf een korte, persoonlijke introductie</li>
    <li>Benadruk jouw inzicht en motivatie voor de rol en de<br>organisatie</li>
  </ul>
</section>

<section class="step orange" style="top:748px">
  <svg class="step-badge" viewBox="0 0 124 124">
    <path d="M62 6A56 56 0 1 0 118 62" fill="none" stroke="var(--orange)" stroke-width="6"/>
    <circle cx="62" cy="62" r="46" fill="var(--orange)"/>
    <text x="62" y="50" text-anchor="middle" font-family="Oswald, sans-serif" font-size="14" fill="#fff">STEP</text>
    <text x="62" y="84" text-anchor="middle" font-family="Oswald, sans-serif" font-weight="700" font-size="34" fill="#fff">04</text>
  </svg>
  <div class="step-title">Controleer en verstuur
    <div class="step-icon"><svg width="26" height="30" viewBox="0 0 26 30"><rect x="2" y="4" width="22" height="24" rx="2" fill="#fff"/><rect x="8" y="1" width="10" height="6" rx="1" fill="#fff" stroke="var(--orange)" stroke-width="1.5"/><path d="M7 17l4 4 8-8" stroke="var(--orange)" stroke-width="2.5" fill="none"/></svg></div>
  </div>
  <ul class="step-list">
    <li>Controleer alle documenten op volledigheid en nauwkeurigheid</li>
    <li>Verstuur je CV, beargumentatie en motivatie per e-mail</li>
    <li>Bevestig de financiële aanbieding per e-mail</li>
  </ul>
</section>

<aside class="extra">
  <div class="extra-label">Extra ondersteuning</div>
  <ul class="extra-list">
    <li>Neem contact op met je toegewezen contactpersoon voor vragen</li>
    <li>Raadpleeg bijgevoegde voorbeeld beargumentatie</li>
  </ul>
</aside>

<p class="tagline">AANDACHT <span>VOOR IMPACT</span></p>

<footer class="footer">
  <div class="recruiter-photo" role="img" aria-label="Profielfoto van de recruiter"></div>
  <div class="recruiter-name">MARK DALEN<small>Recruiter</small></div>
  <div class="contact phone">
    <svg width="16" height="16" viewBox="0 0 16 16"><path d="M3 1l3 3-2 2c1 2 3 4 5 5l2-2 3 3-2 3C6 15 1 10 1 3z" fill="var(--orange)"/></svg>
    0300-481526
  </div>
  <div class="contact mail">
    <svg width="16" height="16" viewBox="0 0 16 16"><rect x="1" y="3" width="14" height="10" rx="1" fill="var(--orange)"/><path d="M1 4l7 5 7-5" stroke="#fff" stroke-width="1.4" fill="none"/></svg>
    info@veltaro.nl
  </div>
  <div class="brand"><span class="brand-mark"></span>VELTARO</div>
</footer>

</body>
</html>
```